One of Australia's fastest growing Financial Company looking for an updated business card design!

Meridale Holdings Australia is looking for an updated design for our business cards. We would like to keep up our professional appearances and have get new exciting design that fits our company.

The Meridale aim is to facilitate and assist clients in every financial requirement that may arise in financial areas.

We would to see the design to use colour blue and we like the clouds in the background. We have attached two designs we have use before but we need something with more professional and easy to read design.

We would like the website in the back of the card; the employees name more central and stands out; only a postal address; a list of all our locations along the bottom (Sydney, Melbourne, Brisbane, Singapore)

Looking forward to seeing the designs come in!

Target Market(s)

Other Industry Professionals
Middle Class Families

Industry/Entity Type

Finance

Contact Information for Business Card

Name; Company Role; Office Number; Mobile Number; Email Address; Website; Postal Address; Locations

Font styles to use
Serif
Sans Serif

Colors
0492cd
33a6d7
85cae6
85acd3
3176b5
0455a3
cee9f5
d5e2ee

Requirements
Must have
• Name; Company Role; Office Number; Mobile Number; Email Address; Website; Postal Address; Locations
Nice to have
• The colour blue, clouds on the background

```html
<!DOCTYPE html>
<html lang="en">
<head>
<meta charset="utf-8">
<title>Meridale Holdings Australia – Business Card</title>
<link rel="stylesheet" href="https://fonts.googleapis.com/css2?family=Montserrat:wght@300;400;600;700&display=swap">
<style>
  :root {
    --backdrop: #0a88d1;
    --brand-blue-light: #33a6d7;
    --brand-blue: #2a82c8;
    --sky-top: #0c63b8;
    --sky-mid: #1f86d3;
    --sky-low: #3b9be0;
    --accent-red: #e83335;
    --paper: #ffffff;
    --ink: #1d1d1f;
    --ink-soft: #3c3c40;
  }
  * { box-sizing: border-box; margin: 0; padding: 0; }
  html, body { width: 1200px; height: 900px; overflow: hidden; }
  body {
    background: var(--backdrop);
    font-family: "Montserrat", sans-serif;
    position: relative;
  }
  .card {
    position: absolute;
    width: 580px;
    height: 350px;
    overflow: hidden;
    box-shadow: 0 10px 24px rgba(0, 40, 90, 0.25);
  }
  .card-front { left: 50px; top: 80px; background: var(--paper); }
  .card-back  { left: 570px; top: 470px; }

  /* front */
  .front-shapes { position: absolute; inset: 0; }
  .front-brand {
    position: absolute;
    left: 0; top: 140px;
    width: 270px;
    display: flex; align-items: center; justify-content: center; gap: 12px;
    color: var(--paper);
    font-weight: 600;
    font-size: 40px;
    letter-spacing: 0.5px;
    white-space: nowrap;
  }
  .brand-dot {
    width: 18px; height: 18px; border-radius: 50%;
    background: var(--paper);
    flex: none;
  }
  .holder {
    position: absolute;
    right: 28px; top: 34px;
    text-align: right;
    color: var(--paper);
    white-space: nowrap;
  }
  .holder-name { font-weight: 700; font-size: 24px; }
  .holder-role { font-weight: 300; font-size: 15px; letter-spacing: 0.4px; margin-top: 2px; }
  .contact-list {
    position: absolute;
    right: 24px; top: 158px;
    list-style: none;
    display: flex; flex-direction: column; gap: 9px;
    font-size: 12.5px;
    color: var(--ink-soft);
    white-space: nowrap;
  }
  .contact-list li { display: flex; justify-content: flex-end; align-items: center; gap: 10px; }
  .contact-icon {
    width: 20px; height: 20px; border-radius: 4px;
    background: var(--accent-red);
    display: flex; align-items: center; justify-content: center;
    flex: none;
  }
  .locations {
    position: absolute;
    right: 24px; bottom: 30px;
    text-align: right;
    font-weight: 600;
    font-size: 12.5px;
    color: var(--ink);
    white-space: nowrap;
  }

  /* back */
  .sky {
    position: absolute; inset: 0;
    background: linear-gradient(160deg, var(--sky-top) 0%, var(--sky-mid) 55%, var(--sky-low) 100%);
  }
  .back-content {
    position: absolute; inset: 0;
    display: flex; flex-direction: column; align-items: center; justify-content: center;
    color: var(--paper);
  }
  .back-brand {
    display: flex; align-items: center; gap: 18px;
    font-weight: 600; font-size: 78px; line-height: 1;
    white-space: nowrap;
  }
  .back-brand .brand-dot { width: 34px; height: 34px; }
  .website {
    margin-top: 18px;
    font-weight: 400; font-size: 20px; letter-spacing: 0.6px;
    white-space: nowrap;
  }
</style>
</head>
<body>

<section class="card card-front" aria-label="Business card front">
  <svg class="front-shapes" width="580" height="350" viewBox="0 0 580 350" aria-hidden="true">
    <defs>
      <linearGradient id="panelBlue" x1="0" y1="0" x2="0" y2="1">
        <stop offset="0" stop-color="#33a6d7"/>
        <stop offset="1" stop-color="#2a82c8"/>
      </linearGradient>
    </defs>
    <rect x="0" y="0" width="280" height="350" fill="url(#panelBlue)"/>
    <polygon points="190,0 580,0 580,112 280,140" fill="#e83335"/>
  </svg>

  <div class="front-brand"><span class="brand-dot"></span>Meridale</div>

  <div class="holder">
    <p class="holder-name">Clara Hensley</p>
    <p class="holder-role">Investment Consultant</p>
  </div>

  <ul class="contact-list">
    <li>0400 555 012
      <span class="contact-icon">
        <svg width="12" height="12" viewBox="0 0 12 12"><rect x="3" y="0.5" width="6" height="11" rx="1.2" fill="none" stroke="#fff" stroke-width="1.2"/><circle cx="6" cy="9.4" r="0.7" fill="#fff"/></svg>
      </span>
    </li>
    <li>(02) 5550 1234
      <span class="contact-icon">
        <svg width="12" height="12" viewBox="0 0 12 12"><path d="M2.2 1 L4.4 1 L5.2 3.6 L3.9 4.6 C4.6 6.2 5.8 7.4 7.4 8.1 L8.4 6.8 L11 7.6 L11 9.8 C11 10.5 10.4 11 9.7 11 C5 10.6 1.4 7 1 2.3 C1 1.6 1.5 1 2.2 1 Z" fill="#fff"/></svg>
      </span>
    </li>
    <li>info@meridaleholdings.com.au
      <span class="contact-icon">
        <svg width="12" height="12" viewBox="0 0 12 12"><rect x="0.8" y="2.5" width="10.4" height="7" rx="0.8" fill="none" stroke="#fff" stroke-width="1.1"/><path d="M1 3 L6 6.8 L11 3" fill="none" stroke="#fff" stroke-width="1.1"/></svg>
      </span>
    </li>
    <li>PO Box 412 Carlingford Vale, NSW 2150
      <span class="contact-icon">
        <svg width="12" height="12" viewBox="0 0 12 12"><path d="M6 11.5 C3.5 8 2.2 6 2.2 4.2 A3.8 3.8 0 0 1 9.8 4.2 C9.8 6 8.5 8 6 11.5 Z" fill="#fff"/><circle cx="6" cy="4.2" r="1.4" fill="#e83335"/></svg>
      </span>
    </li>
  </ul>

  <p class="locations">Sydney | Melbourne | Brisbane | Singapore</p>
</section>

<section class="card card-back" aria-label="Business card back">
  <div class="sky" role="img" aria-label="Photograph of a blue sky with scattered white clouds"></div>
  <div class="back-content">
    <div class="back-brand"><span class="brand-dot"></span>Meridale</div>
    <p class="website">www.meridaleholdings.com.au</p>
  </div>
</section>

</body>
</html>
```